letterhead design for a investing company*

Design an appealing business letterhead to match with our existing logo and attract new customers. Our customers are mainly corporate managers which are detail oriented and judge the company ability to perform a good service based on small details. A professional letterhead will give a good first impression.

Target Market(s)

New customers and business owners

Industry/Entity Type

Marketplace

Font styles to use
Sans Serif
Script

Requirements
Must have
• Must be a professional and elegant design that attracts interest from people who receives it

```html
<!DOCTYPE html>
<html lang="en">
<head>
<meta charset="utf-8">
<title>Brightvale Letterhead</title>
<link href="https://fonts.googleapis.com/css2?family=Poppins:wght@600;700&family=Open+Sans:wght@400;600;700&family=Great+Vibes&display=swap" rel="stylesheet">
<style>
  :root {
    --navy: #13203d;
    --gold: #f6b81c;
    --sky: #2aa6e0;
    --ink: #3b3f47;
    --muted: #6b6f77;
    --paper: #ffffff;
    --backdrop: #ddd0b6;
  }
  * { box-sizing: border-box; }
  html, body {
    margin: 0;
    width: 1200px;
    height: 898px;
    overflow: hidden;
    background: var(--backdrop);
  }
  .letterhead {
    position: absolute;
    left: 310px;
    top: 39px;
    width: 580px;
    height: 820px;
    background: var(--paper);
    box-shadow: 0 14px 30px rgba(80, 60, 30, 0.22);
    font-family: "Open Sans", Arial, sans-serif;
    color: var(--ink);
    overflow: hidden;
  }
  .header-bar {
    position: absolute;
    top: 0; left: 0;
    width: 100%;
    height: 12px;
    background: var(--navy);
    border-bottom: 4px solid var(--gold);
  }
  .brand {
    position: absolute;
    left: 40px;
    top: 58px;
    display: flex;
    align-items: center;
    gap: 10px;
  }
  .brand-dot {
    width: 30px; height: 30px;
    border-radius: 50%;
    background: var(--gold);
  }
  .brand-name {
    font-family: "Poppins", Arial, sans-serif;
    font-weight: 700;
    font-size: 28px;
    color: var(--navy);
  }
  .recipient {
    position: absolute;
    left: 40px;
    top: 150px;
    font-size: 8px;
    line-height: 1.6;
  }
  .recipient-name { color: var(--sky); font-weight: 700; font-size: 9.5px; }
  .recipient-role { font-weight: 600; color: var(--navy); margin-bottom: 4px; }
  .recipient-line b { color: var(--sky); margin-right: 5px; }
  .letter-date {
    position: absolute;
    right: 40px;
    top: 158px;
    font-size: 8px;
    font-weight: 600;
  }
  .letter-body {
    position: absolute;
    left: 40px;
    top: 235px;
    width: 500px;
    font-size: 8.5px;
    line-height: 1.75;
    color: var(--muted);
  }
  .letter-body p { margin: 0 0 12px; }
  .letter-body .greeting { color: var(--navy); font-weight: 600; }
  .closing {
    position: absolute;
    right: 40px;
    top: 470px;
    text-align: right;
    font-size: 8.5px;
    color: var(--muted);
  }
  .closing .script {
    font-family: "Great Vibes", cursive;
    font-size: 26px;
    color: var(--navy);
    line-height: 1.4;
  }
  .sender {
    position: absolute;
    left: 40px;
    top: 598px;
    font-size: 8px;
    line-height: 1.4;
  }
  .sender .script {
    font-family: "Great Vibes", cursive;
    font-size: 24px;
    color: var(--navy);
    line-height: 1.1;
  }
  .sender-name { font-weight: 700; color: var(--navy); }
  .contact {
    position: absolute;
    right: 40px;
    top: 570px;
    list-style: none;
    margin: 0;
    padding: 0;
    font-size: 8px;
    line-height: 1.55;
    text-align: right;
    color: var(--ink);
  }
  .contact li {
    display: flex;
    justify-content: flex-end;
    align-items: flex-start;
    gap: 8px;
    margin-bottom: 5px;
  }
  .contact-icon {
    flex: none;
    width: 14px; height: 14px;
    background: var(--gold);
    display: flex;
    align-items: center;
    justify-content: center;
    margin-top: 1px;
  }
  .footer-bar {
    position: absolute;
    bottom: 0; left: 0;
    width: 100%;
    height: 52px;
    background: var(--navy);
    border-top: 5px solid var(--gold);
    display: flex;
    align-items: center;
    justify-content: center;
  }
  .site-url {
    font-family: "Poppins", Arial, sans-serif;
    font-weight: 600;
    font-size: 11px;
    letter-spacing: 4px;
    color: var(--paper);
  }
</style>
</head>
<body>
  <main class="letterhead">
    <div class="header-bar"></div>

    <div class="brand">
      <span class="brand-dot"></span>
      <span class="brand-name">Brightvale</span>
    </div>

    <div class="recipient">
      <div class="recipient-name">Mara Ellison</div>
      <div class="recipient-role">Chief Director</div>
      <div class="recipient-line"><b>A :</b>18 Harbour Lane Lisbon - 1100</div>
      <div class="recipient-line"><b>P :</b>+351 555 0142</div>
      <div class="recipient-line"><b>E :</b>hello@brightvale.pt</div>
    </div>

    <div class="letter-date">Date: 10 September 2019</div>

    <section class="letter-body">
      <p class="greeting">Dear Mr. Carvalho,</p>
      <p>Thank you for your interest in our investment marketplace. We connect business owners with carefully reviewed opportunities, and every proposal we share is checked for clear terms, realistic returns and sound management.</p>
      <p>Our advisors work closely with each client to understand goals, timelines and tolerance for risk. The result is a portfolio that reflects your priorities and is reported with full transparency every quarter.</p>
      <p>We would welcome the chance to present our current selection in person. Please let us know a convenient date and our team will prepare a tailored briefing.</p>
      <p>This letter outlines the first step of a long partnership built on trust and attention to detail.</p>
    </section>

    <div class="closing">
      <div>Sincerely</div>
      <div class="script">Mara Ellison</div>
    </div>

    <div class="sender">
      <div class="script">Tomas Reyes</div>
      <div class="sender-name">Tomas Reyes</div>
      <div>Manager</div>
    </div>

    <ul class="contact">
      <li><span>+351 555 0142<br>+351 555 0143</span>
        <span class="contact-icon"><svg width="9" height="9" viewBox="0 0 10 10"><path d="M2 1 L4 1 L4.6 3 L3.4 4 Q4.5 6 6 6.6 L7 5.4 L9 6 L9 8 Q9 9 8 9 Q1 8.5 1 2 Q1 1 2 1 Z" fill="#fff"/></svg></span></li>
      <li><span>brightvale-invest.com<br>hello@brightvale.pt</span>
        <span class="contact-icon"><svg width="9" height="9" viewBox="0 0 10 10"><circle cx="5" cy="5" r="4" fill="none" stroke="#fff" stroke-width="1"/><ellipse cx="5" cy="5" rx="1.8" ry="4" fill="none" stroke="#fff" stroke-width="0.8"/><line x1="1" y1="5" x2="9" y2="5" stroke="#fff" stroke-width="0.8"/></svg></span></li>
      <li><span>Harbour Lane 18<br>Lisbon, 1200</span>
        <span class="contact-icon"><svg width="9" height="9" viewBox="0 0 10 10"><path d="M5 9.5 Q1.5 5.5 1.5 3.8 A3.5 3.5 0 0 1 8.5 3.8 Q8.5 5.5 5 9.5 Z" fill="#fff"/><circle cx="5" cy="3.8" r="1.3" fill="var(--gold)"/></svg></span></li>
    </ul>

    <footer class="footer-bar">
      <span class="site-url">www.brightvale.pt</span>
    </footer>
  </main>
</body>
</html>
```